依頼詳細
送付先は、行政関係者、企業の経営者などの専門家を想定しております。
当社のロゴを引き立たせて頂き、高級感があり洗練されたデザインを希望します。
封筒の色は、グレー系を予定しておりますので、フォントの色など調整お願いいたします。
記載項目
住所、会社名、会社ロゴ、電話番号、FAX番号、WEBアドレス
希望イメージ
シンプル 複雑
単色 カラフル
暗い 明るい
日常 高級
遊び心 厳粛
未来的 伝統的
女性的 男性的
希望する色
納品ファイル
• イラストレーター形式 (.ai)
補足説明
希望のデザインの色ですが、青色系でお願いいたします。

添付フャイルが上がっておりませんでしたので、添付いたします。

またデザインは、イラストレータ(ai形式)とjpg形式の2種類
の製作をお願いたします。

よろしくおねがいいたします。

の製作をお願いたします。

よろしくおねがいいたします。
■ 選んだ理由

シンプルかつ上品なデザインでしたので、こちらを選ばせて頂きました。

■ 提案者全員のお礼・コメント

たくさんの提案を頂き、ありがとうございます。
今後ともご縁がありましたら、宜しく御願い申し上げます。

```html
<!DOCTYPE html>
<html lang="ja">
<head>
<meta charset="utf-8">
<title>Envelope – Minato Consulting</title>
<link rel="stylesheet" href="https://fonts.googleapis.com/css2?family=Noto+Sans+JP:wght@400;500;700&family=Noto+Serif:wght@700&display=swap">
<style>
  :root {
    --navy: #1b2a5e;
    --paper: #f1f1f2;
    --edge: #d9d9dc;
    --stage: #ffffff;
    --ink: #1b2a5e;
    --ink-soft: #3a4468;
  }
  html, body {
    margin: 0;
    padding: 0;
    width: 807px;
    height: 1200px;
    overflow: hidden;
    background: var(--stage);
  }
  .envelope {
    position: absolute;
    left: 22px;
    top: 22px;
    width: 763px;
    height: 1151px;
    background: var(--paper);
    box-shadow: 0 0 0 1px var(--edge);
    font-family: "Noto Sans JP", sans-serif;
  }
  .envelope__flap {
    position: absolute;
    left: 0;
    top: 0;
    width: 763px;
    height: 126px;
  }
  .brand {
    position: absolute;
    left: 40px;
    top: 850px;
    width: 340px;
    display: flex;
    flex-direction: column;
    align-items: center;
  }
  .brand__mark {
    width: 150px;
    height: 150px;
    background: var(--navy);
  }
  .brand__name {
    margin: 28px 0 0;
    font-family: "Noto Serif", serif;
    font-size: 24px;
    font-weight: 700;
    color: var(--navy);
    white-space: nowrap;
  }
  .divider {
    position: absolute;
    left: 380px;
    top: 895px;
    width: 5px;
    height: 196px;
    background: var(--navy);
  }
  .contact {
    position: absolute;
    left: 430px;
    top: 928px;
    color: var(--ink);
  }
  .contact__company {
    margin: 0 0 22px;
    font-size: 17px;
    font-weight: 500;
    letter-spacing: 0.04em;
  }
  .contact__lines {
    margin: 0;
    font-size: 11px;
    line-height: 20px;
    color: var(--ink-soft);
    letter-spacing: 0.02em;
  }
</style>
</head>
<body>
  <div class="envelope">
    <svg class="envelope__flap" viewBox="0 0 763 126" aria-hidden="true">
      <rect x="0" y="0" width="763" height="126" fill="var(--navy)"/>
    </svg>

    <div class="brand">
      <div class="brand__mark" aria-hidden="true"></div>
      <p class="brand__name">Minato Consulting Inc.</p>
    </div>

    <div class="divider"></div>

    <div class="contact">
      <p class="contact__company">株式会社ミナトコンサルティング</p>
      <p class="contact__lines">
        〒800-0012 北九州市門司区港町2-4-6 港町ビル5階<br>
        TEL 093-000-1234　FAX 093-000-5678<br>
        URL http://www.minato-consult.example.jp
      </p>
    </div>
  </div>
</body>
</html>
```